GHalvor Busisness Card

I am an aerospace consultant and at this time only need business cards.

Industry/Entity Type

Business

Contact Information for Business Card

Halvorsen Associates,LLC
Marcus D. Halvorsen

348 Birch Meadow Drive
Hartwell AL 35612

256-555-0187 (cell)
256-555-0142 (fax)

marcushalvorsen@mailbrook.test

```html
<!DOCTYPE html>
<html lang="en">
<head>
<meta charset="utf-8">
<title>Halvorsen Associates – Business Card</title>
<link rel="stylesheet" href="https://fonts.googleapis.com/css2?family=Ubuntu:wght@400;500;700&display=swap">
<style>
  :root {
    --backdrop: #e9e6e1;
    --card: #000000;
    --ink: #f2f2f2;
    --ink-muted: #8a8a8a;
    --card-shadow: rgba(0, 0, 0, 0.28);
  }
  * { margin: 0; padding: 0; box-sizing: border-box; }
  html, body {
    width: 1200px;
    height: 1000px;
    overflow: hidden;
    background: var(--backdrop);
  }
  .canvas {
    position: relative;
    width: 1200px;
    height: 1000px;
  }
  .business-card {
    position: absolute;
    left: 180px;
    top: 260px;
    width: 840px;
    height: 480px;
    background: var(--card);
    box-shadow: 0 10px 30px var(--card-shadow);
    font-family: "Ubuntu", sans-serif;
    color: var(--ink);
  }
  .brand {
    position: absolute;
    left: 24px;
    width: 420px;
    top: 264px;
    text-align: center;
  }
  .brand-name {
    font-size: 34px;
    font-weight: 500;
    letter-spacing: -0.3px;
    color: var(--ink);
  }
  .brand-tagline {
    margin-top: 2px;
    font-size: 18px;
    font-weight: 400;
    color: var(--ink-muted);
  }
  .contact {
    position: absolute;
    left: 470px;
    top: 124px;
  }
  .person-name {
    font-size: 25px;
    font-weight: 700;
    letter-spacing: 0.3px;
  }
  .person-role {
    font-size: 19px;
    margin-top: 2px;
  }
  .address {
    margin-top: 44px;
    font-size: 21px;
    line-height: 1.4;
  }
  .phones {
    margin-top: 12px;
    font-size: 21px;
    line-height: 1.4;
  }
  .email {
    margin-top: 12px;
    font-size: 21px;
  }
  .label { display: inline-block; min-width: 26px; }
</style>
</head>
<body>
  <main class="canvas">
    <section class="business-card">
      <div class="brand">
        <div class="brand-name">HalvorsenAssociates</div>
        <div class="brand-tagline">your aerospace consultant</div>
      </div>
      <div class="contact">
        <div class="person-name">Marcus D. Halvorsen</div>
        <div class="person-role">Consultant</div>
        <div class="address">
          348 Birch Meadow Drive<br>
          Hartwell AL 35612
        </div>
        <div class="phones">
          <span class="label">M :</span> 256-555-0187<br>
          <span class="label">F :</span> 256-555-0142
        </div>
        <div class="email"><span class="label">E :</span> marcushalvorsen@mailbrook.test</div>
      </div>
    </section>
  </main>
</body>
</html>
```